Business Card Design for a Technology Development Company

******* PLEASE NOTE (ALL DESIGNERS): I am going to finish the competition on Monday the 9th July (NOT SATURDAY 15TH). I have some designs I like and need to get them printed next week. Please submit any designs today or tomorrow. *******

PLEASE READ ALL OF THE REQUIREMENTS!!! I've rejected lot's of designs in the past because they didn't read the basic requirements - thanks and good luck!

Quill Harbor is a UK technology / small holding company that invests in startups and develops new ideas. In addition it provides IT Professional Services.

Ideally the design will be simple, professional, smart, and sophisticated, and overall be nice to look at. You can be creative as you like with the design, equally as simple as you like - you guys are the professionals so I'll leave it to your inspiration (make sure you incorporate the logo)!
Updates

PLEASE NOTE (ALL DESIGNERS): I am going to finish the competition on Monday the 9th July (NOT SATURDAY 15TH).  I have some designs I like and need to get them printed next week.  Please submit any designs today or tomorrow.

Target Market(s)

Enterprises / corporations / public sector / technical engineers / investors. More www.brantelix.com / www.vornel.com than www.pibbleroo.com!

Industry/Entity Type

Business

Requirements
Must have
• It should be modern and any artwork (if used) should be simple
- Pastel colours, dark and light colours, and shades are preferred over bright colours
- The design should incorporate the attached Quill Harbor logo and the logo colour scheme
- The logo should be on both sides. The back should just have the logo, maybe with some additional graphics
- It must have the following information on:

FirstName SecondName
Company Position
Email: name@quillharbor.co.uk
Mobile: +44 (0) 7700 984312

- The final design should be for a UK business card, dimensions: 85mm × 55mm
- The final design should have bleed marks to allow for printing and should be given in vector formats (EPS and AI)
Nice to have
• The Logo can be separated from the font in the logo on the front of the card. This isn't necessary or required, just to know it's not a limitation.
Should not have
• No bright colours (I prefer pastel colours, dark and light colours, and shades)
- Fonts that are to thin
- Effects or designs that make it difficult to print
- Italic or old fashioned looking fonts, i.e. anything like Times New Roman is a NO!

```html
<!DOCTYPE html>
<html lang="en">
<head>
<meta charset="utf-8">
<title>Quill Harbor – Business Cards</title>
<link href="https://fonts.googleapis.com/css2?family=Comfortaa:wght@600&family=PT+Serif&family=Open+Sans:wght@400&display=swap" rel="stylesheet">
<style>
  :root {
    --backdrop: #e9e6e1;
    --card-black: #050607;
    --card-charcoal: #2e2f30;
    --card-white: #ffffff;
    --teal-deep: #0f8aa5;
    --teal-logo: #5cbccf;
    --teal-faint: #d6ebf2;
    --ink: #1c1c1c;
  }
  * { margin: 0; padding: 0; box-sizing: border-box; }
  html, body { width: 1200px; height: 900px; overflow: hidden; }
  body {
    background: var(--backdrop);
    position: relative;
  }
  .card {
    position: absolute;
    top: 275px;
    width: 540px;
    height: 350px;
    border-radius: 22px;
    overflow: hidden;
    box-shadow: 0 10px 28px rgba(0,0,0,.22);
  }
  .card--back {
    left: 40px;
    background: linear-gradient(160deg, var(--card-charcoal) 0%, #1b1c1d 38%, var(--card-black) 40%, var(--card-black) 100%);
  }
  .card--front { left: 620px; background: var(--card-white); }
  .card__art { position: absolute; inset: 0; width: 100%; height: 100%; }

  .wordmark {
    position: absolute;
    display: flex;
    align-items: center;
    gap: 12px;
    font-family: "Comfortaa", sans-serif;
    font-weight: 600;
    color: var(--teal-logo);
    white-space: nowrap;
  }
  .wordmark__dot {
    border-radius: 50%;
    background: var(--teal-logo);
    flex: none;
  }
  .card--back .wordmark {
    left: 50%; top: 50%;
    transform: translate(-50%, -50%);
    font-size: 46px;
  }
  .card--back .wordmark__dot { width: 40px; height: 40px; }
  .card--front .wordmark {
    left: 18px; top: 118px;
    font-size: 18px;
    gap: 7px;
  }
  .card--front .wordmark__dot { width: 16px; height: 16px; }

  .holder {
    position: absolute;
    left: 250px; top: 54px;
    display: flex;
    flex-direction: column;
    align-items: flex-end;
  }
  .holder__name {
    font-family: "PT Serif", serif;
    font-size: 30px;
    color: var(--teal-deep);
    line-height: 1.1;
  }
  .holder__role {
    font-family: "PT Serif", serif;
    font-size: 15px;
    color: var(--ink);
    margin-top: 2px;
  }
  .contact {
    position: absolute;
    left: 250px;
    bottom: 34px;
    list-style: none;
    font-family: "Open Sans", sans-serif;
    font-size: 15px;
    color: var(--teal-deep);
  }
  .contact__item { display: flex; align-items: center; gap: 7px; margin-top: 10px; }
  .contact__icon { width: 15px; height: 15px; flex: none; }
</style>
</head>
<body>

  <section class="card card--back" aria-label="Card back">
    <div class="wordmark"><span class="wordmark__dot"></span>Quill Harbor</div>
  </section>

  <section class="card card--front" aria-label="Card front">
    <svg class="card__art" viewBox="0 0 540 350" preserveAspectRatio="none" aria-hidden="true">
      <circle cx="470" cy="150" r="70" fill="var(--teal-faint)" opacity=".7"/>
      <path d="M0 0 H230 C190 110 160 230 150 350 H0 Z" fill="var(--card-black)"/>
      <path d="M230 0 C190 110 160 230 150 350 H162 C170 230 196 110 240 0 Z" fill="var(--card-white)"/>
      <path d="M240 0 C196 110 170 230 162 350 H178 C182 230 206 110 250 0 Z" fill="var(--teal-deep)"/>
    </svg>

    <div class="wordmark"><span class="wordmark__dot"></span>Quill Harbor</div>

    <div class="holder">
      <p class="holder__name">Elliot Marsh</p>
      <p class="holder__role">Company Position</p>
    </div>

    <ul class="contact">
      <li class="contact__item">
        <svg class="contact__icon" viewBox="0 0 16 16" aria-hidden="true"><rect x="1" y="3" width="14" height="10" fill="none" stroke="currentColor" stroke-width="1.4"/><path d="M1 3 L8 9 L15 3" fill="none" stroke="currentColor" stroke-width="1.4"/></svg>
        name@quillharbor.co.uk
      </li>
      <li class="contact__item">
        <svg class="contact__icon" viewBox="0 0 16 16" aria-hidden="true"><rect x="4" y="1" width="8" height="14" rx="1.5" fill="currentColor"/><rect x="5.5" y="3" width="5" height="8" fill="#fff"/></svg>
        +44 (0) 7700 984312
      </li>
    </ul>
  </section>

</body>
</html>
```